WordPress Site Design and Code for Technology Consulting Startup

We need a WordPress design and code to a new site on Tallow Bay. We have the logo and colors ready. The site will be a brochure site with a CONTACT page that contains a form that the prospective client fills out. The other pages would be ABOUT / SERVICES (3 option drop-down) / SUPPORT. The site should be appropriate for an IT Consulting / IT Managed Services / IT Project Management services in the Chicago area.

Across small, medium, large businesses.

Technology, network infrastructure, IT.

Coded - Design and coding required

5+ page

• I prefer mid-modern / simple / art deco / minimalist.

```html
<!DOCTYPE html>
<html lang="en">
<head>
<meta charset="utf-8">
<title>Corvane — IT Consulting</title>
<link href="https://fonts.googleapis.com/css2?family=Audiowide&family=Poppins:wght@400;500;600;700&display=swap" rel="stylesheet">
<style>
:root{
  --ink:#2f2b2a;
  --text:#555;
  --muted:#777;
  --orange:#f47a20;
  --teal:#1b97b0;
  --grey-bg:#f4f4f4;
  --field:#eeeeee;
  --line:#e6e6e6;
  --white:#fff;
}
*{margin:0;padding:0;box-sizing:border-box}
html,body{width:1200px;height:3354px;overflow:hidden}
body{position:relative;font-family:"Poppins",sans-serif;color:var(--text);background:var(--white)}
.abs{position:absolute}
.display{font-family:"Audiowide",sans-serif;color:var(--ink);font-weight:400}
.brand{font-family:"Poppins",sans-serif;font-weight:700;color:var(--ink);letter-spacing:2px;display:flex;align-items:center;gap:10px}
.brand .mark{display:inline-block;background:var(--orange)}
.btn-dark{background:var(--ink);color:var(--white);font-weight:600;font-size:12px;display:flex;align-items:center;justify-content:center;text-transform:uppercase}

/* header */
.site-header{left:0;top:0;width:1200px;height:91px;border-bottom:1px solid var(--line);background:var(--grey-bg)}
.site-header .brand{position:absolute;left:88px;top:26px;font-size:28px}
.site-header .brand .mark{width:34px;height:34px}
.nav{position:absolute;left:671px;top:0;height:91px;display:flex;gap:31px;font-size:13px;font-weight:500;color:var(--ink)}
.nav a{display:flex;align-items:center;height:91px;text-decoration:none;color:inherit;position:relative}
.nav a.active{color:var(--orange)}
.nav a.active::before{content:"";position:absolute;top:0;left:-6px;right:-6px;height:3px;background:var(--orange)}
.nav-cta{left:993px;top:27px;width:118px;height:35px;font-size:12px}

/* hero */
.hero-bg{left:0;top:91px;width:1200px;height:444px;background:var(--grey-bg)}
.hero-title{left:0;top:148px;width:1200px;text-align:center;font-size:41px;line-height:44px}
.hero-sub{left:0;top:254px;width:1200px;text-align:center;font-size:16.5px;color:var(--text)}
.hero-photo{left:88px;top:335px;width:1023px;height:533px;background:linear-gradient(135deg,#8a7d70,#c9b7a3 45%,#6f6459)}

/* about */
.about-mark{left:172px;top:990px;width:348px;height:300px;display:flex;align-items:center;justify-content:center;gap:14px;font-size:38px}
.about-mark .mark{width:40px;height:40px}
.eyebrow{left:592px;top:968px;font-size:12.5px;font-weight:600;color:var(--ink);display:flex;align-items:center;gap:10px}
.eyebrow::before{content:"";width:40px;height:1px;background:#ccc}
.about-title{left:592px;top:998px;width:460px;font-size:29.5px;line-height:31.5px}
.about-text{left:592px;top:1108px;width:440px;font-size:14.5px;line-height:22.3px}
.about-btn{left:595px;top:1264px;width:128px;height:40px}

/* services */
.services-band{left:0;top:1420px;width:1200px;height:365px;background:var(--teal)}
.services-title{left:0;top:1487px;width:1200px;text-align:center;font-size:29px;color:var(--white)}
.card{top:1550px;width:295px;height:398px;background:var(--white);box-shadow:0 10px 30px rgba(0,0,0,.08)}
.card .photo{height:234px}
.card h3{position:absolute;left:25px;top:264px;font-family:"Audiowide",sans-serif;font-weight:400;font-size:16px;color:var(--ink)}
.card p{position:absolute;left:25px;top:292px;width:250px;font-size:13.5px;line-height:19.5px}
.card .go{position:absolute;left:225px;top:381px;width:37px;height:37px;background:var(--orange)}

/* form */
.form-title{left:0;top:2056px;width:1200px;text-align:center;font-size:29px}
.form-sub{left:0;top:2098px;width:1200px;text-align:center;font-size:13.5px;color:var(--ink)}
.field label{display:block;font-size:12.5px;font-weight:600;color:var(--ink);height:20px}
.field label span{color:var(--orange)}
.field .input{width:375px;height:47px;background:var(--field);font-size:13px;color:var(--muted);padding:15px 17px}
.field .input.area{width:767px;height:117px}
.submit{left:514px;top:2578px;width:173px;height:46px;font-size:15px;font-weight:700}

/* cta */
.cta-band{left:0;top:2742px;width:1200px;height:194px;background:linear-gradient(90deg,#f47a20,#f58a33 50%,#f47a20)}
.cta-brand{left:88px;top:2792px;width:107px;height:92px;display:flex;align-items:center;justify-content:center}
.cta-brand .mark{width:60px;height:60px;border:6px solid var(--white)}
.cta-text{left:222px;top:2797px;font-size:29px;line-height:37px;color:var(--white)}
.cta-btn{left:993px;top:2822px;width:117px;height:35px;background:var(--white);color:var(--ink);font-size:12px;font-weight:600;display:flex;align-items:center;justify-content:center}

/* footer */
.foot-brand{left:88px;top:3090px;font-size:34px}
.foot-brand .mark{width:42px;height:42px}
.socials{left:139px;top:3155px;display:flex;gap:9px}
.socials span{width:38px;height:38px;border-radius:50%;background:#eee}
.foot-col h4{font-family:"Audiowide",sans-serif;font-weight:400;font-size:17px;color:var(--ink);margin-bottom:18px}
.foot-col ul{list-style:none;font-size:12.5px;color:var(--ink)}
.links li{height:31px}
.contact li{display:flex;gap:10px;margin-bottom:16px;line-height:18px}
.contact svg{flex:none;margin-top:2px}
.news p{font-size:12.5px;line-height:18px;color:var(--ink);width:230px}
.news .input{margin-top:20px;width:260px;height:47px;background:var(--grey-bg);display:flex;align-items:center;padding:0 18px;gap:8px;font-size:12.5px;color:var(--muted)}
.news .input .send{margin-left:auto}
.foot-rule{left:88px;top:3303px;width:1023px;height:1px;background:var(--line)}
.copyright{left:0;top:3318px;width:1200px;text-align:center;font-size:12.5px;font-weight:500;color:var(--ink)}
.to-top{left:1133px;top:3281px;width:42px;height:42px;border-radius:50%;background:var(--teal);display:flex;align-items:center;justify-content:center}
</style>
</head>
<body>

<header class="abs site-header">
  <div class="brand"><span class="mark"></span>CORVANE</div>
  <nav class="nav">
    <a class="active" href="#">HOME</a>
    <a href="#">ABOUT</a>
    <a href="#">SERVICES <svg width="10" height="10" viewBox="0 0 10 10" style="margin-left:4px"><path d="M2 3.5l3 3 3-3" fill="none" stroke="#2f2b2a" stroke-width="1.4"/></svg></a>
    <a href="#">SUPPORT</a>
  </nav>
</header>
<div class="abs btn-dark nav-cta">CONTACT US</div>

<section>
  <div class="abs hero-bg"></div>
  <h1 class="abs display hero-title">Smooth Business Starts With<br>Good Sewrvice Consultation</h1>
  <p class="abs hero-sub">IT Consulting / IT Managed Services / IT Project Management services</p>
  <div class="abs hero-photo" role="img" aria-label="Photo of a team of consultants talking around a table with laptops"></div>
</section>

<section>
  <div class="abs brand about-mark"><span class="mark"></span>CORVANE</div>
  <div class="abs eyebrow">ABOUT US</div>
  <h2 class="abs display about-title">We Provide The Best Solution Your Business Development</h2>
  <p class="abs about-text">Aenean sollicitudin, lorem quis bibendum auctor, nisi elit consequat ipsum, nec sagittis sem nibh id elit. Duis sed odio sit amet nibh vulputate cursus a sit amet mauris. Morbi accumsan ipsum velit. Nam nec tellus a odio tincidunt auctor a ornare odio. Sed non &nbsp;mauris vitae erat consequat auctor eu in elit class aptent taciti...</p>
  <div class="abs btn-dark about-btn">LEARN MORE</div>
</section>

<section>
  <div class="abs services-band"></div>
  <h2 class="abs display services-title">Our Services</h2>
  <article class="abs card" style="left:143px">
    <div class="photo" role="img" aria-label="Photo of colleagues gathered around a phone in an office" style="background:linear-gradient(135deg,#d9dde0,#a9a49c)"></div>
    <h3>IT Consulting</h3>
    <p>Aenean sollicitudin, lorem quis duis bibendum auctor nisi elit consequat ipsum nec sagittis sem nibh...</p>
    <div class="go"><svg width="37" height="37" viewBox="0 0 37 37"><path d="M16 13l5 5.5-5 5.5" fill="none" stroke="#fff" stroke-width="1.8"/></svg></div>
  </article>
  <article class="abs card" style="left:452px">
    <div class="photo" role="img" aria-label="Photo of two businessmen working at a laptop" style="background:linear-gradient(135deg,#e4e2de,#5b5f68)"></div>
    <h3>IT Managed</h3>
    <p>Aenean sollicitudin, lorem quis duis bibendum auctor nisi elit consequat ipsum nec sagittis sem nibh...</p>
    <div class="go"><svg width="37" height="37" viewBox="0 0 37 37"><path d="M16 13l5 5.5-5 5.5" fill="none" stroke="#fff" stroke-width="1.8"/></svg></div>
  </article>
  <article class="abs card" style="left:762px">
    <div class="photo" role="img" aria-label="Photo of a presenter leading a meeting in a conference room" style="background:linear-gradient(135deg,#cfd3d6,#6c6a6e)"></div>
    <h3>IT Project Management</h3>
    <p>Aenean sollicitudin, lorem quis duis bibendum auctor nisi elit consequat ipsum nec sagittis sem nibh...</p>
    <div class="go"><svg width="37" height="37" viewBox="0 0 37 37"><path d="M16 13l5 5.5-5 5.5" fill="none" stroke="#fff" stroke-width="1.8"/></svg></div>
  </article>
</section>

<section>
  <h2 class="abs display form-title">Fill Out The Form Below</h2>
  <p class="abs form-sub">The more details the better and Let’s see if &nbsp;I can help tou.</p>
  <div class="abs field" style="left:216px;top:2157px"><label>First Name<span>*</span></label><div class="input">Enter first name</div></div>
  <div class="abs field" style="left:608px;top:2157px"><label>Last Name<span>*</span></label><div class="input">Enter Last Name</div></div>
  <div class="abs field" style="left:216px;top:2241px"><label>Email<span>*</span></label><div class="input">Enter your email</div></div>
  <div class="abs field" style="left:608px;top:2241px"><label>Phone<span>*</span></label><div class="input">Enter phone number</div></div>
  <div class="abs field" style="left:216px;top:2325px"><label>Company<span>*</span></label><div class="input">Enter company name</div></div>
  <div class="abs field" style="left:608px;top:2325px"><label>Subject<span>*</span></label><div class="input">Enter subject</div></div>
  <div class="abs field" style="left:216px;top:2409px"><label>Message<span>*</span></label><div class="input area">Type your text</div></div>
  <div class="abs btn-dark submit">SUBMIT NOW</div>
</section>

<section>
  <div class="abs cta-band"></div>
  <div class="abs cta-brand"><span class="mark"></span></div>
  <h2 class="abs display cta-text">When Do We Start? We’re Ready To<br>Assist You! Connect With Us Today.</h2>
  <div class="abs cta-btn">SUPPORT</div>
</section>

<footer>
  <div class="abs brand foot-brand"><span class="mark"></span>CORVANE</div>
  <div class="abs socials"><span></span><span></span><span></span><span></span></div>

  <div class="abs foot-col links" style="left:454px;top:3033px">
    <h4>Quick links</h4>
    <ul><li>Home</li><li>About Us</li><li>Services</li><li>Support</li><li>Contact Us</li></ul>
  </div>

  <div class="abs foot-col contact" style="left:625px;top:3033px">
    <h4>Contact info</h4>
    <ul>
      <li><svg width="13" height="10" viewBox="0 0 13 10"><rect width="13" height="10" rx="1" fill="var(--teal)"/><path d="M1 1l5.5 4.5L12 1" fill="none" stroke="#fff" stroke-width="1.2"/></svg><div>Email:<br>hello@corvane.example</div></li>
      <li><svg width="13" height="13" viewBox="0 0 13 13"><path d="M3 1l2 3-1.3 1.3a7 7 0 0 0 4 4L9 8l3 2-1 2.2C6 12.5 .5 7 .8 2z" fill="var(--teal)"/></svg><div>Phone:<br>+1 312 555 0148</div></li>
      <li><svg width="12" height="15" viewBox="0 0 12 15"><path d="M6 15S0 8.5 0 5.5a6 6 0 0 1 12 0C12 8.5 6 15 6 15z" fill="var(--teal)"/><circle cx="6" cy="5.5" r="2" fill="#fff"/></svg><div>Location:<br>Some address line here<br>United Kingdom</div></li>
    </ul>
  </div>

  <div class="abs foot-col news" style="left:851px;top:3035px">
    <h4>Newsletter</h4>
    <p>Subscribe to our email address to get the latest news.</p>
    <div class="input"><svg width="13" height="10" viewBox="0 0 13 10"><rect width="13" height="10" rx="1" fill="#aaa"/><path d="M1 1l5.5 4.5L12 1" fill="none" stroke="#fff" stroke-width="1.2"/></svg>Enter your email...<svg class="send" width="16" height="16" viewBox="0 0 16 16"><path d="M15 1L1 7l5 2 2 6z" fill="var(--teal)"/></svg></div>
  </div>

  <div class="abs foot-rule"></div>
  <p class="abs copyright">© Copyright 2023, All Rights Reserved</p>
  <div class="abs to-top"><svg width="14" height="16" viewBox="0 0 14 16"><path d="M7 14V2M2 7l5-5 5 5" fill="none" stroke="#fff" stroke-width="1.5"/></svg></div>
</footer>

</body>
</html>
```